Lotus Nest Product Marketing Sheet Front and Back

Please see the VERY VERY VERY ROUGH COMPS THAT WE DID TO LEND SOME DIRECTION TO THE PIECE- SO YOU HAVE AN IDEA OF WHAT'S IMPORTANT TO COMMUNICATE ON THE FRONT AND THE BACK.

DON'T FOLLOW OUR LAYOUT.. This is just for you to see what goes to the front and what goes to the back.. see the files that we just loaded up to the art folder!

We also have a PDF that has a check off list for items that need to be on the front and then on the back!

PROJECT SCOPE:

Project is to make a sell sheet front that is 8.5 inches wide x 11 inches tall in a 4 color design using our current Lotus Nest Logo with your design talents. We also need the back of the sell sheet that has the basic instructions on how to install the Lotus Nest Mattress Cover and shows the value added aspects of the product.

We need files in layered PSD format as we have various dealers that we tweak parts of our product line. We will also use these layered files as a back up for the printer in case they don't have the printer font, we can make him print ready file from your PSD file.

We have the logo, tag line, header main font selected and need you to design the look and feel of the piece.

We have all of the copy for the sell sheet- this is the only PDF file in the art file resources.

Overall this piece needs to convey a FUN, FRESH and PEACEFUL PRODUCT.. we don't want a cluttered design.

Updates

Reason: We have a lot of designers that have requested a few more days to submit.. so we are extending the competition. Thank you and good luck!

Target Market(s)

Shopwell Consumers that are buying a mattress cover for comfort, peace of mind and to reduce night heat issues ( sweating) and to avoid dust mites, bed bugs and stains.

Industry/Entity Type

Marketing

Font styles to use
Sans Serif

Colors
f37122
f68e4e
fabb94
0393ce
33a6d7
86cae7
ffffff
add136
fbee3d

Requirements
Must have
• Our Current Logo as the center piece..
• LOTUS NEST is the brand name
• For a peaceful night sleep is the tag line
• Value Points ( see the PDF attached)
• Crisp color, Clean Fonts, Cant be cluttered.
• File Construction- Must be a PSD file 8.5 x11 and 300 DPI for printing
Nice to have
• Clean, Easy to Read and consistent from the front to the back
Should not have
• We don't want a cluttered look and feel for this marketing piece.

```html
<!DOCTYPE html>
<html lang="en">
<head>
<meta charset="utf-8">
<title>Lotus Nest Sell Sheet – Front and Back</title>
<link href="https://fonts.googleapis.com/css2?family=Roboto:ital,wght@0,400;0,500;0,700;1,700;1,900&family=Roboto+Condensed:wght@400;700&family=Lato:ital,wght@1,300;1,400&display=swap" rel="stylesheet">
<style>
  :root{
    --lime:#add136;
    --orange:#f37122;
    --orange-soft:#f68e4e;
    --blue:#0393ce;
    --sky:#33a6d7;
    --sky-pale:#86cae7;
    --white:#ffffff;
    --ink:#2b2b2b;
    --stage:#2c2d2f;
  }
  *{margin:0;padding:0;box-sizing:border-box}
  html,body{width:1200px;height:891px;overflow:hidden;background:var(--stage)}
  .sheet{position:absolute;top:104px;width:655px;height:847px;transform:scale(.8);transform-origin:0 0;overflow:hidden;background:var(--lime);font-family:"Roboto",sans-serif}
  .sheet--front{left:68px}
  .sheet--back{left:616px}
  .sheet-bg{position:absolute;inset:0;width:655px;height:847px}
  .abs{position:absolute}

  /* brand */
  .brand-name{left:40px;top:112px;font:700 22px/1 "Roboto",sans-serif;color:var(--orange);letter-spacing:.5px;display:flex;align-items:center;gap:8px}
  .brand-mark{width:22px;height:22px;border-radius:50%;background:var(--orange)}
  .tagline{left:40px;top:143px;font:300 italic 21px/1 "Lato",sans-serif;color:var(--sky)}

  .headline{right:28px;top:47px;text-align:right;color:var(--white)}
  .headline-kicker{font:italic 900 21px/25px "Roboto",sans-serif}
  .headline-fit{font:400 33px/32px "Roboto",sans-serif;margin-top:8px}

  /* feature badges */
  .badge{position:absolute;border-radius:50%;background:var(--white);border:5px solid var(--sky);box-shadow:0 2px 6px rgba(0,0,0,.2);display:flex;align-items:center;justify-content:center;overflow:hidden}
  .badge svg{width:70%;height:70%}
  .badge-fill{width:100%;height:100%;border-radius:50%}
  .fill-splash{background:radial-gradient(circle at 50% 50%,var(--sky) 0 34%,var(--sky-pale) 35% 42%,var(--white) 43%)}
  .fill-mite{background:radial-gradient(circle at 42% 38%,#6cc0e6 0%,#2a87c0 45%,#0d4f80 75%,var(--white) 76%)}
  .fill-soft{background:linear-gradient(135deg,#f0f0f0 0%,#fbfbfb 45%,#e2e2e2 70%,#d7c4b6 100%)}
  .fill-allergen{background:radial-gradient(circle at 40% 45%,#1d9ad4 0 40%,var(--white) 41%)}
  .feature-label{position:absolute;font:400 18px/17px "Roboto Condensed",sans-serif;color:var(--blue);text-align:center}
  .feature-label--left{text-align:left}

  .photo{position:absolute}

  /* footer */
  .perk{position:absolute;top:790px;font:italic 700 14px/16px "Roboto",sans-serif;color:var(--white);text-align:center}
  .crown{position:absolute;top:798px;width:18px;height:16px}
  .sold{position:absolute;right:28px;top:733px;text-align:right;font:700 18px/21px "Roboto",sans-serif;color:var(--white)}
  .retailer{font:700 25px/1 "Roboto",sans-serif;color:var(--ink);margin-top:6px}

  /* back */
  .steps-number{left:30px;top:88px;font:700 68px/1 "Roboto",sans-serif;color:var(--lime)}
  .steps-title{left:74px;top:101px;font:italic 700 23px/23px "Roboto",sans-serif;color:var(--lime)}
  .step-ring{position:absolute;top:70px;width:108px;height:108px;border-radius:50%;border:6px solid var(--lime);background:var(--white)}
  .row-label{position:absolute;top:413px;font:400 11px/13px "Roboto Condensed",sans-serif;color:var(--blue);text-align:center;width:80px;margin-left:-40px}
  .sizes-title{left:0;width:655px;top:470px;text-align:center;font:500 27px/1 "Roboto",sans-serif;color:var(--orange)}
  .size{position:absolute;background:var(--orange);color:var(--white);text-align:center;padding-top:30px;box-shadow:0 2px 4px rgba(0,0,0,.15)}
  .size-name{font:700 16px/17px "Roboto Condensed",sans-serif}
  .size-dim{font:400 10px/14px "Roboto Condensed",sans-serif;margin-top:4px}
  .offer-title{left:194px;top:734px;font:700 30px/1 "Roboto",sans-serif;color:var(--white)}
  .offer-text{left:195px;top:772px;font:400 15px/19px "Roboto",sans-serif;color:var(--white)}
</style>
</head>
<body>

<svg width="0" height="0" style="position:absolute" aria-hidden="true">
  <defs>
    <linearGradient id="iconBlue" x1="0" y1="0" x2="0" y2="1">
      <stop offset="0" stop-color="#86cae7"/><stop offset="1" stop-color="#0393ce"/>
    </linearGradient>
    <symbol id="icon-drop" viewBox="0 0 100 100"><path d="M50 8 C64 32 78 48 78 66 A28 28 0 0 1 22 66 C22 48 36 32 50 8Z" fill="url(#iconBlue)"/><ellipse cx="40" cy="62" rx="5" ry="11" fill="#fff" opacity=".6"/></symbol>
    <symbol id="icon-sound" viewBox="0 0 100 100"><g fill="none" stroke="#0393ce" stroke-width="6" stroke-linecap="round"><path d="M40 36 A18 18 0 0 1 40 64"/><path d="M28 28 A28 28 0 0 1 28 72" transform="translate(-6 0)"/><path d="M56 30 C74 26 80 46 70 56 C64 62 66 72 58 74"/><path d="M60 46 C64 42 70 46 66 52"/></g></symbol>
    <symbol id="icon-bacteria" viewBox="0 0 100 100"><g fill="url(#iconBlue)"><rect x="16" y="28" width="18" height="44" rx="9"/><rect x="41" y="28" width="18" height="44" rx="9"/><rect x="66" y="28" width="18" height="44" rx="9"/></g><g fill="#fff"><circle cx="25" cy="40" r="3"/><circle cx="25" cy="58" r="3"/><circle cx="50" cy="40" r="3"/><circle cx="50" cy="58" r="3"/><circle cx="75" cy="40" r="3"/><circle cx="75" cy="58" r="3"/></g></symbol>
    <symbol id="icon-washer" viewBox="0 0 100 100"><rect x="16" y="12" width="68" height="78" rx="8" fill="url(#iconBlue)"/><rect x="16" y="12" width="68" height="16" rx="6" fill="#0b6fa3"/><circle cx="28" cy="20" r="3" fill="#fff"/><circle cx="40" cy="20" r="3" fill="#fff"/><circle cx="50" cy="58" r="22" fill="#fff"/><circle cx="50" cy="58" r="15" fill="#0393ce"/><circle cx="50" cy="58" r="7" fill="#86cae7"/></symbol>
  </defs>
</svg>

<!-- FRONT -->
<section class="sheet sheet--front" aria-label="Sell sheet front">
  <svg class="sheet-bg" viewBox="0 0 655 847" aria-hidden="true">
    <defs>
      <linearGradient id="frontWhite" x1="0" y1="0" x2="0" y2="1">
        <stop offset="0" stop-color="#ffffff"/><stop offset="1" stop-color="#f1f1f1"/>
      </linearGradient>
    </defs>
    <path d="M0,0 H290 C500,90 640,280 652,420 C650,600 500,760 320,768 C190,772 80,720 0,655 Z" fill="url(#frontWhite)"/>
  </svg>

  <div class="photo" role="img" aria-label="Photo of a young girl sleeping on a white pillow hugging a plush toy"
       style="left:0;top:165px;width:480px;height:430px;border-radius:0 48% 40% 0/0 45% 55% 0;background:linear-gradient(100deg,#c2825a 0%,#e2ad86 22%,#f2d3bb 42%,#f4e7d8 62%,#f7f3ee 80%,rgba(247,243,238,0) 100%)"></div>

  <div class="abs brand-name"><span class="brand-mark"></span>LOTUS NEST</div>
  <div class="abs tagline">for a peaceful night sleep</div>

  <div class="abs headline">
    <div class="headline-kicker">Terry Cloth Waterproof<br>Mattress Protection</div>
    <div class="headline-fit">FITS CAL<br>KING</div>
  </div>

  <div class="badge" style="left:322px;top:175px;width:58px;height:58px;border-width:4px"><svg><use href="#icon-sound"/></svg></div>
  <div class="feature-label feature-label--left" style="left:384px;top:192px">Quite</div>

  <div class="badge" style="left:407px;top:239px;width:58px;height:58px;border-width:4px"><svg><use href="#icon-bacteria"/></svg></div>
  <div class="feature-label feature-label--left" style="left:472px;top:251px">Bacteria<br>Free</div>

  <div class="badge" style="left:474px;top:307px;width:72px;height:72px"><div class="badge-fill fill-soft" role="img" aria-label="Photo of a hand on soft terry cloth"></div></div>
  <div class="feature-label feature-label--left" style="left:554px;top:328px">Ultra<br>Soft</div>

  <div class="badge" style="left:508px;top:403px;width:94px;height:94px"><div class="badge-fill fill-allergen" role="img" aria-label="Icon of a person breathing clean air"></div></div>
  <div class="feature-label" style="left:515px;top:502px;width:80px">Allergen<br>Free</div>

  <div class="badge" style="left:449px;top:540px;width:108px;height:108px"><svg><use href="#icon-washer"/></svg></div>
  <div class="feature-label" style="left:463px;top:653px;width:80px">Washable</div>

  <div class="badge" style="left:32px;top:482px;width:138px;height:138px;border-width:6px"><svg><use href="#icon-drop"/></svg></div>
  <div class="feature-label" style="left:51px;top:624px;width:100px">Waterproof</div>

  <div class="badge" style="left:177px;top:570px;width:120px;height:120px"><div class="badge-fill fill-splash" role="img" aria-label="Illustration of a sweat stain splash"></div></div>
  <div class="feature-label" style="left:177px;top:696px;width:120px">SWEAT<br>Stain Blocker</div>

  <div class="badge" style="left:322px;top:603px;width:108px;height:108px"><div class="badge-fill fill-mite" role="img" aria-label="Illustration of a dust mite"></div></div>
  <div class="feature-label" style="left:326px;top:716px;width:100px">Dust Mite</div>

  <div class="perk" style="left:22px;width:110px">FIVE SIDED<br>PROTECTION</div>
  <svg class="crown" style="left:137px" viewBox="0 0 18 16" aria-hidden="true"><path d="M1,4 L5,9 L9,2 L13,9 L17,4 L15,13 H3 Z M3,14 H15 V16 H3 Z" fill="#fff"/></svg>
  <div class="perk" style="left:165px;width:140px">ELASTIC CORNERS<br>FOR EXTRA GRIP</div>
  <svg class="crown" style="left:313px" viewBox="0 0 18 16" aria-hidden="true"><path d="M1,4 L5,9 L9,2 L13,9 L17,4 L15,13 H3 Z M3,14 H15 V16 H3 Z" fill="#fff"/></svg>
  <div class="perk" style="left:340px;width:142px">NO SLIP MATTRESS<br>PROTECTION</div>

  <div class="sold">SOLD<br>EXCLUSIVELY<br>ON<div class="retailer">Shopwell</div></div>
</section>

<!-- BACK -->
<section class="sheet sheet--back" aria-label="Sell sheet back">
  <svg class="sheet-bg" viewBox="0 0 655 847" aria-hidden="true">
    <path d="M0,0 H440 C530,40 610,100 655,165 V700 C420,725 140,690 0,575 Z" fill="#ffffff"/>
  </svg>

  <div class="photo" role="img" aria-label="Photo of water spilling from a tipped glass onto a white terry cloth cover, with a hand pressing the fabric"
       style="left:0;top:175px;width:655px;height:300px;background:linear-gradient(180deg,#f7f7f7 0%,#ebebeb 35%,#f1f1f1 70%,#fafafa 100%)"></div>

  <div class="abs steps-number">3</div>
  <div class="abs steps-title">Simple<br>Steps to Install</div>
  <div class="step-ring" style="left:266px"></div>
  <div class="step-ring" style="left:381px"></div>
  <div class="step-ring" style="left:492px"></div>

  <div class="badge" style="left:28px;top:329px;width:56px;height:56px;border-width:4px"><svg><use href="#icon-drop"/></svg></div>
  <div class="row-label" style="left:56px">WATERPROOF</div>
  <div class="badge" style="left:90px;top:325px;width:64px;height:64px;border-width:4px"><div class="badge-fill fill-splash" role="img" aria-label="Stain splash illustration"></div></div>
  <div class="row-label" style="left:122px">SWEAT<br>STAIN BLOCKER</div>
  <div class="badge" style="left:158px;top:317px;width:80px;height:80px;border-width:4px"><div class="badge-fill fill-mite" role="img" aria-label="Dust mite illustration"></div></div>
  <div class="row-label" style="left:198px">DUST MITE</div>
  <div class="badge" style="left:242px;top:311px;width:92px;height:92px;border-width:4px"><svg><use href="#icon-washer"/></svg></div>
  <div class="row-label" style="left:288px">WASHABLE</div>
  <div class="badge" style="left:337px;top:311px;width:92px;height:92px;border-width:4px"><div class="badge-fill fill-soft" role="img" aria-label="Photo of a hand on soft terry cloth"></div></div>
  <div class="row-label" style="left:383px">ULTRA<br>SOFT</div>
  <div class="badge" style="left:432px;top:319px;width:76px;height:76px;border-width:4px"><div class="badge-fill fill-allergen" role="img" aria-label="Icon of a person breathing clean air"></div></div>
  <div class="row-label" style="left:470px">ALLERGEN<br>FREE</div>
  <div class="badge" style="left:514px;top:327px;width:60px;height:60px;border-width:4px"><svg><use href="#icon-bacteria"/></svg></div>
  <div class="row-label" style="left:544px">BACTERIA<br>FREE</div>
  <div class="badge" style="left:582px;top:330px;width:54px;height:54px;border-width:4px"><svg><use href="#icon-sound"/></svg></div>
  <div class="row-label" style="left:609px">QUITE</div>

  <div class="abs sizes-title">Available in these sizes:</div>
  <div class="size" style="left:47px;top:512px;width:49px;height:94px"><div class="size-name">TWIN</div><div class="size-dim">39" X 75"</div></div>
  <div class="size" style="left:104px;top:512px;width:51px;height:100px"><div class="size-name">TWIN<br>XL</div><div class="size-dim" style="margin-top:0">39" X 80"</div></div>
  <div class="size" style="left:163px;top:512px;width:70px;height:96px"><div class="size-name">FULL</div><div class="size-dim">54" X 80"</div></div>
  <div class="size" style="left:242px;top:512px;width:76px;height:100px"><div class="size-name">QUEEN</div><div class="size-dim">60" X 80"</div></div>
  <div class="size" style="left:327px;top:512px;width:91px;height:104px"><div class="size-name">CAL<br>KING</div><div class="size-dim">76" X 84"</div></div>
  <div class="size" style="left:426px;top:512px;width:97px;height:100px"><div class="size-name">KING</div><div class="size-dim">76" X 80"</div></div>
  <div class="size" style="left:531px;top:512px;width:72px;height:100px"><div class="size-name">DOUBLE</div><div class="size-dim">53" X 79.5"</div></div>

  <div class="photo" role="img" aria-label="Photo of three stacked white pillows"
       style="left:18px;top:712px;width:158px;height:106px;border-radius:18px;background:linear-gradient(180deg,#ffffff 0%,#eef0ef 50%,#dfe3e0 100%)"></div>

  <div class="abs offer-title">We also offer:</div>
  <div class="abs offer-text">Lotus Nest Pillows<br>and Pillow Cases</div>

  <div class="sold">SOLD<br>EXCLUSIVELY<br>ON<div class="retailer">Shopwell</div></div>
</section>

</body>
</html>
```